Laminated Training Card; highly professional yet engaging, colorful, fits branding

We need an 8 1/2" x 11" piece, printed front and back, to inspire and offer instructions for nonprofit leaders on key coaching skills to use with their staff. Though it's in a professional services setting, this piece communicates a sense of fun and excitement to encourage leaders to try out these skills, and keep the training card close at hand. An infographic style would be ideal.

Target Market(s)

Nonprofit leaders will use the laminated training card in a face to face training class, and then take it back to the office to use to 'train' their staff

Industry/Entity Type

Training

Font styles to use
Serif

Requirements
Must have
• See project brief attached
Nice to have
Should not have

```html
<!DOCTYPE html>
<html lang="en">
<head>
<meta charset="utf-8">
<title>Northpath Center – Accountability Culture Training Card</title>
<link href="https://fonts.googleapis.com/css2?family=Montserrat:wght@400;500;600;700&display=swap" rel="stylesheet">
<style>
  :root{
    --backdrop:#2e2d30;
    --paper:#e8e3e2;
    --body-bg:#dcd8d7;
    --panel-gray:#d6d1cf;
    --orange:#dc572a;
    --gold:#f3a922;
    --blue:#5bbde0;
    --green:#adbd3a;
    --charcoal:#58585a;
    --ink:#3d3a3b;
    --brown:#6b4c3e;
    --white:#ffffff;
  }
  *{margin:0;padding:0;box-sizing:border-box}
  html,body{width:1200px;height:1200px;overflow:hidden;background:var(--backdrop)}
  body{font-family:'Montserrat',sans-serif;color:var(--ink)}
  .card{position:absolute;left:222px;top:42px;width:774px;height:1094px;background:var(--paper);overflow:hidden}
  .abs{position:absolute}

  .header{left:0;top:0;width:662px;height:117px;background:var(--paper)}
  .brand{left:0;top:0;width:662px;height:117px;display:flex;align-items:center;justify-content:center;gap:14px;color:var(--brown);font-weight:500}
  .brand-mark{width:54px;height:54px;border-radius:50%;background:var(--brown);flex:none}
  .brand-name{font-size:31px;line-height:1.1;letter-spacing:-0.3px}
  .brand-name small{display:block;font-size:22px;font-weight:500}

  .gutter{left:662px;top:0;width:9px;height:547px;background:var(--white);opacity:.85}
  .hero-photo{left:0;top:117px;width:662px;height:305px;
    background:linear-gradient(90deg,#d6e0dc 0%,#eef2f1 45%,#e3e9ec 70%,#d9e1e5 100%)}
  .side-top{left:671px;top:117px;width:103px;height:305px;background:var(--panel-gray)}
  .band{left:0;top:422px;width:662px;height:125px;background:var(--orange)}
  .side-band{left:671px;top:422px;width:103px;height:125px;background:var(--orange)}
  .headline{right:138px;top:459px;text-align:right;color:var(--white);font-size:21.5px;font-weight:500;letter-spacing:1.4px;line-height:27px;text-transform:uppercase;white-space:nowrap}
  .headline .accent{color:var(--gold)}
  .vision{left:722px;top:170px;transform-origin:0 0;transform:translateX(18px) rotate(90deg);
    font-size:33px;font-weight:600;letter-spacing:13px;color:rgba(255,255,255,.6);white-space:nowrap;line-height:36px}

  .content-photo{left:0;top:547px;width:662px;height:547px;
    background:radial-gradient(circle at 40% 55%,#e2dfde 0%,#d8d4d3 55%,#cfcbca 100%)}
  .side-green{left:662px;top:547px;width:112px;height:462px;background:var(--green)}
  .corner-block{left:554px;top:1009px;width:220px;height:85px;background:var(--charcoal)}
  .left-green{left:0;top:853px;width:84px;height:241px;background:var(--green)}
  .left-rule{left:80px;top:1014px;width:8px;height:80px;background:var(--charcoal)}

  .tip{left:134px;width:496px}
  .tip-head{display:flex;align-items:flex-end;gap:12px;margin-bottom:18px}
  .tip-num{font-size:54px;font-weight:700;line-height:42px;letter-spacing:-2px}
  .tip-title{font-size:17.5px;font-weight:700;color:var(--ink);line-height:20px}
  .tip p{font-size:11.2px;font-weight:500;line-height:13.6px;margin-bottom:13px;color:var(--ink)}
  .tip-one{top:578px}
  .tip-one .tip-num{color:var(--blue)}
  .tip-two{top:822px}
  .tip-two .tip-num{color:var(--gold)}
  .tip-two .tip-head{gap:16px}
</style>
</head>
<body>
<main class="card">
  <header class="abs header"></header>
  <div class="abs brand">
    <span class="brand-mark"></span>
    <span class="brand-name">Northpath Center<small>for Nonprofit Leadership</small></span>
  </div>

  <div class="abs hero-photo" role="img" aria-label="Photo of a confident businesswoman in an office beside a chess king among pawns"></div>
  <div class="abs side-top"></div>
  <div class="abs band"></div>
  <div class="abs side-band"></div>
  <div class="abs gutter"></div>
  <div class="abs vision">OUR VISION</div>
  <h1 class="abs headline">Create an accountability culture with<br>teams and alliesvaluable <span class="accent">tips for success</span></h1>

  <div class="abs content-photo" role="img" aria-label="Faint background photo of a compass dial pointing to leadership"></div>
  <div class="abs side-green"></div>
  <div class="abs corner-block"></div>
  <div class="abs left-green"></div>
  <div class="abs left-rule"></div>

  <section class="abs tip tip-one">
    <div class="tip-head"><span class="tip-num">01</span><h2 class="tip-title">POWERFUL QUESTIONS</h2></div>
    <p>Coach yourself asking powerful questions; they break your internal monologue. Ask others a powerful question – that you don’t answer.&nbsp; They will feel deeply heard.</p>
    <p>Dream one moment: What’s possible? And establish accountability the next: What should I do when you miss your deadline?</p>
    <p>Asking questions isn’t reserved for the leader. Whoever asks the powerful questions is the leader in the moment.</p>
    <p>With whom is it safe to ask powerful questions in your culture?</p>
  </section>

  <section class="abs tip tip-two">
    <div class="tip-head"><span class="tip-num">02</span><h2 class="tip-title">4 DIMENSIONS OF LEADERSHIP</h2></div>
    <p>Knowing when to move between these stances = leadership mastery.</p>
    <p>Leading from the front: eyes on the vision and staying connected to those who follow<br>Leading from the side:&nbsp; locking arms in the company of equals. Eyes on the shared vision, but each has their own path to get there.</p>
    <p>Leading from behind: ‘fading’ while still holding the space. You’ve got their backs.<br>Leading from above: seeing the big picture</p>
  </section>
</main>
</body>
</html>
```